Multifamily Investment Strategies

I need a pamphlet or booklet for multifamily commercial real estate investment.

The specific investment vehicle is affordable multifamily apartments. I have uploaded a 5 page pdf detailing my investment strategy.

The target audience for this pamphlet are investors, commercial brokers, and commercial bankers.

I am looking for modern, clean design that is striking and professional but also eye catching.
Updates

I made a few changes to the brief and also corrected two errors.

Target Market(s)

Commercial Real Estate Investors, Brokers, and Bankers

Industry/Entity Type

Real Estate

Font styles to use
Serif

Colors

Designer to choose colors to be used in the design.

Requirements
Must have
• Graphics of or related to apartment buildings.
• My headshot seen on the last page of the pdf
Nice to have
• Imagery related to investment and profits.
Should not have
• The image of an apartment building on the first page of the pdf is just an example. Please don’t use this image.

```html
<!DOCTYPE html>
<html lang="en">
<head>
<meta charset="utf-8">
<title>Multifamily Cashflow Investment Strategy – Page 4</title>
<link rel="stylesheet" href="https://fonts.googleapis.com/css2?family=PT+Sans:wght@400;700&family=Questrial&family=Roboto:wght@400&display=swap">
<style>
  :root {
    --accent: #d4834f;
    --ink: #1a1a1a;
    --muted: #4a4a4a;
    --panel: #f4f4f4;
    --rule: #b8b8b8;
    --page: #ffffff;
    --photo-a: #5f86a6;
    --photo-b: #a49686;
  }
  * { margin: 0; padding: 0; box-sizing: border-box; }
  html, body { width: 927px; height: 1200px; overflow: hidden; background: var(--page); }
  .page { position: relative; width: 927px; height: 1200px; background: var(--page); }
  .page-rule { position: absolute; left: 0; width: 927px; height: 1px; background: var(--rule); }
  .page-rule.top { top: 0; }
  .page-rule.bottom { top: 1198px; }

  .running-head {
    position: absolute; right: 94px; top: 58px;
    font: 400 15.2px/1 "Roboto", Arial, sans-serif;
    color: var(--ink);
  }
  .running-head .accent { color: var(--accent); }

  .panel { position: absolute; left: 91px; top: 82px; width: 746px; height: 1041px; background: var(--panel); }

  .hero-photo {
    position: absolute; left: 55px; top: 188px; width: 872px; height: 492px;
    background: linear-gradient(135deg, var(--photo-a) 0%, var(--photo-b) 100%);
  }

  .title-box {
    position: absolute; left: 129px; top: 128px; width: 436px; height: 144px;
    background: var(--accent); color: #fff;
    padding: 30px 0 0 62px;
    font: 400 33px/46px "Questrial", "Century Gothic", sans-serif;
  }

  .strategy-list { position: absolute; left: 124px; top: 0; width: 700px; list-style: none; }
  .strategy {
    position: absolute; left: 0; white-space: nowrap;
    font: 700 19px/1 "PT Sans", "Myriad Pro", sans-serif; color: var(--ink);
  }
  .detail {
    position: absolute; left: 55px; width: 600px;
    font: 400 14.3px/19px "PT Sans", "Myriad Pro", sans-serif; color: var(--ink);
  }
  .detail::before {
    content: ""; position: absolute; left: -14px; top: 7px;
    width: 5px; height: 5px; border-radius: 50%; background: var(--accent);
  }
  .detail .lead { color: var(--accent); }

  .footer-name {
    position: absolute; left: 91px; top: 1145px;
    font: 400 15px/1 "Roboto", Arial, sans-serif; color: var(--muted);
  }
  .page-number {
    position: absolute; right: 94px; top: 1145px;
    font: 400 15px/1 "Roboto", Arial, sans-serif; color: var(--accent);
  }
</style>
</head>
<body>
<div class="page">
  <div class="page-rule top"></div>

  <p class="running-head">MULTIFAMILY CASHFLOW <span class="accent">INVESTMENT STRATEGY</span></p>

  <div class="panel"></div>
  <div class="hero-photo" role="img" aria-label="Photograph of a three-storey apartment complex with balconies"></div>

  <h1 class="title-box">5 STRATEGIES FOR<br>INCREASING INCOME</h1>

  <ol class="strategy-list">
    <li class="strategy" style="top:716px">1. Fill Vacant Units at Market Rate</li>
    <li class="detail" style="top:750px"><span class="lead">After light renovation (&lt; $1,000 per unit)</span> - modern, two-tone paint schemes (white trim, taupe/light grey walls); vinyl wood plank flooring to replace carpet; cleaning of existing carpet.</li>

    <li class="strategy" style="top:808px">2. Employ RUBS, where applicable</li>
    <li class="detail" style="top:840px"><span class="lead">Pre-calculated formula</span> for billing back a tenant’s utilities.</li>
    <li class="detail" style="top:864px"><span class="lead">Water, sewer, trash, gas/electric.</span></li>

    <li class="strategy" style="top:900px">3. Gradually raise existing tenants to market rate AFTER adding value</li>
    <li class="detail" style="top:932px;width:660px"><span class="lead">Improve the exterior “curb appeal”</span> - power washing, landscaping, painting. Inexpensive and effective.</li>

    <li class="strategy" style="top:977px">4. Fees - Pet fees; deposits; late fees (without exception); move-in fees</li>
    <li class="strategy" style="top:1020px">5. Laundry machines</li>
    <li class="strategy" style="top:1065px">6. Lower expenses through renegotiation of contracts</li>
  </ol>

  <p class="footer-name">Dana Whitfield, Real Estate Investor.</p>
  <p class="page-number">4</p>

  <div class="page-rule bottom"></div>
</div>
</body>
</html>
```